Young adult personal development needs podcast 1400x1400 logo

We need artwork done for a podcast logo. The podcast is called The Brightmakers Show and is aimed at ages 20-30 waking up and wanting to make changes in their lives.

Using either of the two photos with the logo at bottom right of picture.

Somewhere it says: The Brightmakers Show: Educating & inspiring you to reach your greatest potential.

"The Brightmakers Show: Educating & inspiring you to reach your greatest potential.

With a strong belief in mentors and role models being a key factor to anyones success, Callum has placed himself along side the best in their fields.

Diving into movement, primal patterns, mindfulness, creativity and even the influence our gut has over our brain, these experts are going to show you how these pieces paint the picture that is your greatest potential."

```html
<!DOCTYPE html>
<html lang="en">
<head>
<meta charset="utf-8">
<title>The Brightmakers Show – Podcast Cover</title>
<link rel="stylesheet" href="https://fonts.googleapis.com/css2?family=Vidaloka&family=Vollkorn:wght@600&display=swap">
<style>
  :root {
    --teal-light: #52c2d0;
    --teal-dark: #1d6a71;
    --frame-soft: #86bcc1;
    --white: #ffffff;
    --ink-teal: #1a5d63;
    --bubble-green: rgba(84, 180, 128, 0.62);
    --bubble-tan: rgba(196, 168, 104, 0.72);
    --bubble-beige: rgba(214, 204, 150, 0.72);
    --bubble-lime: rgba(96, 186, 84, 0.8);
  }
  html, body {
    margin: 0;
    padding: 0;
    width: 1200px;
    height: 1200px;
    overflow: hidden;
    background: var(--teal-dark);
  }
  .cover {
    display: block;
    width: 1200px;
    height: 1200px;
  }
  .bg-top { fill: var(--teal-light); }
  .bg-bottom { fill: var(--teal-dark); }
  .frame-outer { fill: none; stroke: var(--frame-soft); stroke-width: 18; }
  .frame-inner { fill: none; stroke: var(--white); stroke-width: 12; }
  .stripes line { stroke: rgba(255, 255, 255, 0.35); stroke-width: 4; }
  .title-box { fill: none; stroke: var(--white); stroke-width: 7; }
  .title {
    font-family: "Vidaloka", serif;
    fill: var(--white);
    font-size: 45px;
    letter-spacing: 1.5px;
    text-anchor: middle;
  }
  .tagline {
    font-family: "Vollkorn", serif;
    font-weight: 600;
    fill: var(--ink-teal);
    font-size: 27px;
    text-anchor: middle;
  }
  .host-photo { fill: url(#photoTones); }
  .bubble-green { fill: var(--bubble-green); }
  .bubble-tan { fill: var(--bubble-tan); }
  .bubble-beige { fill: var(--bubble-beige); }
  .bubble-lime { fill: var(--bubble-lime); }
  .brand-dot { fill: none; stroke: var(--white); stroke-width: 2; }
  .brand-name {
    font-family: "Vidaloka", serif;
    fill: var(--white);
    font-size: 14px;
    letter-spacing: 1px;
  }
</style>
</head>
<body>
<svg class="cover" viewBox="0 0 900 900" xmlns="http://www.w3.org/2000/svg">
  <defs>
    <radialGradient id="photoTones" cx="50%" cy="55%" r="60%">
      <stop offset="0%" stop-color="#e7a48c"/>
      <stop offset="45%" stop-color="#d9b780"/>
      <stop offset="80%" stop-color="#4d6b34"/>
      <stop offset="100%" stop-color="#2c3f22"/>
    </radialGradient>
    <clipPath id="cornerTL"><rect x="0" y="0" width="170" height="150"/></clipPath>
    <clipPath id="cornerBR"><rect x="690" y="620" width="210" height="280"/></clipPath>
  </defs>

  <!-- background bands -->
  <rect class="bg-top" x="0" y="0" width="900" height="590"/>
  <rect class="bg-bottom" x="0" y="588" width="900" height="312"/>

  <!-- corner stripes -->
  <g class="stripes" clip-path="url(#cornerTL)">
    <line x1="0" y1="40" x2="40" y2="0"/>
    <line x1="0" y1="70" x2="70" y2="0"/>
    <line x1="0" y1="100" x2="100" y2="0"/>
    <line x1="0" y1="130" x2="130" y2="0"/>
    <line x1="10" y1="150" x2="160" y2="0"/>
  </g>
  <g class="stripes" clip-path="url(#cornerBR)">
    <line x1="620" y1="900" x2="900" y2="620"/>
    <line x1="650" y1="900" x2="900" y2="650"/>
    <line x1="680" y1="900" x2="900" y2="680"/>
    <line x1="710" y1="900" x2="900" y2="710"/>
    <line x1="740" y1="900" x2="900" y2="740"/>
    <line x1="770" y1="900" x2="900" y2="770"/>
    <line x1="800" y1="900" x2="900" y2="800"/>
  </g>

  <!-- frames -->
  <rect class="frame-outer" x="31" y="31" width="838" height="838"/>
  <rect class="frame-inner" x="50" y="50" width="800" height="800"/>

  <!-- title -->
  <rect class="title-box" x="138" y="88" width="626" height="136"/>
  <text class="title" x="451" y="147">THE BRIGHTMAKERS</text>
  <text class="title" x="451" y="205">SHOW</text>

  <!-- tagline -->
  <text class="tagline" x="450" y="283">Educating &amp; inspiring you to reach your</text>
  <text class="tagline" x="450" y="322">greatest potential.</text>

  <!-- host photo -->
  <circle class="host-photo" cx="452" cy="590" r="238" role="img" aria-label="Portrait photo of the host Callum laughing outdoors in front of green foliage"/>

  <!-- bubbles -->
  <circle class="bubble-green" cx="226" cy="474" r="52"/>
  <circle class="bubble-tan" cx="182" cy="506" r="30"/>
  <circle class="bubble-beige" cx="706" cy="585" r="46"/>
  <circle class="bubble-lime" cx="722" cy="674" r="24"/>
  <circle class="bubble-tan" cx="628" cy="806" r="45"/>

  <!-- brand, bottom right -->
  <circle class="brand-dot" cx="690" cy="811" r="8"/>
  <text class="brand-name" x="704" y="816">RVB BRIGHTWORK</text>
</svg>
</body>
</html>
```